Online Spanish language company requires a book cover design.

We need a book cover design for a Spanish workbook that deals with what is often seen as a frightening grammar topic. The book is going to be called. 'Unlocking the Spanish Conditional Mood' with an extra sidebar which says: 'Take a breath and tackle the Conditional today!'

The idea of the book is to show students that it isn't that difficult and so the cover should reflect that. The key ideas are, safe/easy/structured/do-able.

The size of the book is 15.24 cm by 22.86cm

The authors are Warren Hale-Ortega and Beatrice Hale-Ortega

The book will have between 250 and 300 pages. We will have to confirm this once it is finished so that the spine can be adjusted accordingly.

Target Market(s)

English speaking market. Ages from 20 to 70 with a focus on 40 -60 age group.

Industry/Entity Type

It Company

Font styles to use
Sans Serif

Colors
fbee3e
ec1f27

Requirements
Must have
• Must have the feel of fun while maintaining an element of professionalism.
• On the back it must have a QR code (we will supply)
• Our BrightPath Spanish logo.
• A write up on the back about the contents and the authors.
Nice to have
• We are open to all ideas.
Should not have
• Let's not have flags or donkeys or flamenco. haha.

```html
<!DOCTYPE html>
<html lang="en">
<head>
<meta charset="utf-8">
<title>Unlocking the Spanish Conditional Mood – Cover Options</title>
<link rel="stylesheet" href="https://fonts.googleapis.com/css2?family=Open+Sans:wght@300;400;600;700;800&display=swap">
<style>
  :root {
    --page: #ffffff;
    --cover-yellow: #fccc00;
    --glow: #fffbe6;
    --maroon: #5e0000;
    --band-red: #a80000;
    --title-red: #ec1f27;
    --title-dark: #a30d12;
    --author-dark: #6b0a0a;
    --label-grey: #3d4a55;
    --line-white: #ffffff;
  }
  * { box-sizing: border-box; margin: 0; padding: 0; }
  html, body {
    width: 1200px; height: 900px; overflow: hidden;
    background: var(--page);
    font-family: "Open Sans", Arial, sans-serif;
  }
  .sheet { position: relative; width: 1200px; height: 900px; }

  .cover {
    position: absolute; top: 45px; width: 539px; height: 809px;
    background: var(--cover-yellow); overflow: hidden;
  }
  .cover--one { left: 39px; }
  .cover--two { left: 622px; }

  .option-label {
    position: absolute; right: 0; bottom: 2px;
    font-size: 26px; font-weight: 400; color: var(--label-grey);
  }

  .title {
    position: absolute; font-weight: 800; letter-spacing: -0.5px;
    background: linear-gradient(to bottom, var(--title-red) 0%, var(--title-red) 45%, var(--title-dark) 100%);
    -webkit-background-clip: text; background-clip: text; color: transparent;
    line-height: 1;
  }
  .title-tick { position: absolute; width: 6px; }

  .brand { position: absolute; display: flex; align-items: center; gap: 6px; }
  .brand-dot { border-radius: 50%; background: var(--title-red); }
  .brand-name { font-weight: 300; color: var(--title-red); line-height: 1.05; }

  /* option one */
  .cover--one .glow {
    position: absolute; left: -40px; top: -130px; width: 440px; height: 560px;
    background: radial-gradient(ellipse at 50% 50%, var(--glow) 0%, rgba(255,251,230,0.7) 22%, rgba(252,204,0,0) 68%);
  }
  .spine-bar { position: absolute; left: 0; width: 37px; background: var(--maroon); }
  .spine-bar--top { top: 0; height: 50px; }
  .spine-bar--main { top: 269px; bottom: 0; }
  .cover--one .brand { left: 25px; top: 132px; }
  .cover--one .brand-dot { width: 46px; height: 46px; }
  .cover--one .brand-name { font-size: 14px; }
  .cover--one .title { left: 80px; top: 258px; font-size: 48px; }
  .cover--one .title-tick { left: 256px; top: 302px; height: 56px; background: var(--title-dark); }
  .cover--one .authors {
    position: absolute; left: 272px; top: 316px;
    font-size: 10.5px; font-weight: 700; color: var(--author-dark); line-height: 14px;
  }

  /* option two */
  .light-panel { position: absolute; left: 126px; top: 15px; width: 268px; height: 355px; }
  .guides { position: absolute; left: 0; top: 0; }
  .cover--two .title { left: 128px; top: 336px; font-size: 33px; }
  .cover--two .title-tick { left: 259px; top: 368px; height: 57px; background: var(--band-red); }
  .cover--two .authors {
    position: absolute; left: 0; width: 539px; top: 663px; text-align: center;
    font-size: 13px; line-height: 18px;
  }
  .authors-heading { font-weight: 700; color: var(--author-dark); }
  .authors-names { font-weight: 400; color: #fff4c7; }
  .footer-band { position: absolute; left: 0; top: 719px; width: 539px; height: 51px; background: var(--band-red); }
  .cover--two .brand { left: 20px; top: 703px; gap: 10px; }
  .cover--two .brand-dot { width: 66px; height: 66px; }
  .cover--two .brand-name { font-size: 18px; color: var(--cover-yellow); }
</style>
</head>
<body>
<main class="sheet">

  <section class="cover cover--one" aria-label="Cover option one">
    <div class="glow"></div>
    <div class="spine-bar spine-bar--top"></div>
    <div class="spine-bar spine-bar--main"></div>
    <div class="brand">
      <span class="brand-dot"></span>
      <span class="brand-name">BrightPath<br>Spanish</span>
    </div>
    <h1 class="title">UNLOCKING</h1>
    <div class="title-tick"></div>
    <p class="authors">The authors<br>Warren Hale-Ortega and<br>Beatrice Hale-Ortega</p>
    <span class="option-label">option_1</span>
  </section>

  <section class="cover cover--two" aria-label="Cover option two">
    <svg class="light-panel" viewBox="0 0 268 355" role="img" aria-label="Bright burst of light receding into a corridor of rays">
      <defs>
        <radialGradient id="burst" cx="0.5" cy="0.5" r="0.6">
          <stop offset="0" stop-color="#ffffff"/>
          <stop offset="0.35" stop-color="#fff3b0"/>
          <stop offset="1" stop-color="#ffe066"/>
        </radialGradient>
      </defs>
      <rect width="268" height="355" fill="url(#burst)"/>
    </svg>
    <svg class="guides" width="539" height="809" viewBox="0 0 539 809" aria-hidden="true">
      <g stroke="var(--line-white)" stroke-width="1.2">
        <line x1="82" y1="82" x2="436" y2="82"/>
        <line x1="82" y1="368" x2="436" y2="368"/>
        <line x1="126" y1="55" x2="126" y2="410"/>
        <line x1="394" y1="55" x2="394" y2="410"/>
      </g>
    </svg>
    <h1 class="title">UNLOCKING</h1>
    <div class="title-tick"></div>
    <div class="authors">
      <p class="authors-heading">The Authors</p>
      <p class="authors-names">Warren Hale-Ortega and<br>Beatrice Hale-Ortega</p>
    </div>
    <div class="footer-band"></div>
    <div class="brand">
      <span class="brand-dot"></span>
      <span class="brand-name">BrightPath<br>Spanish</span>
    </div>
    <span class="option-label">option_2</span>
  </section>

</main>
</body>
</html>
```